Professional Business Cards

We need a nice looking, profession and modern business card for our new company. Our logo is attatched

Target Market(s)

Young Professionals

Industry/Entity Type

Financial

Contact Information for Business Card

FRONT

Vardane Ledger Pty Ltd
Level 22, Harbour Point, 48 Wattlebrook Ave
Sydney NSW 2000
ABN : 47 318 905 226

Owen Hadley - Chief Operations Officer
P : 02 9173 5528
M: 0418 356 091
owen@vardaneledger,com

BACK

- Cryptocurrency Exchange Services
- Cryptocurrency Mining Operations
- Cryptocurrency Investment Fund Offering

Font styles to use
Sans Serif

Colors
0255a3
9d9d9d

```html
<!DOCTYPE html>
<html lang="en">
<head>
<meta charset="utf-8">
<title>Vardane Ledger Business Card</title>
<link href="https://fonts.googleapis.com/css2?family=Montserrat:wght@400;500;700&display=swap" rel="stylesheet">
<style>
  :root {
    --brand-blue: #0255a3;
    --brand-grey: #9d9d9d;
    --text-grey: #5c5c5c;
    --paper: #ffffff;
    --backdrop: #e9e7e4;
  }
  * { margin: 0; padding: 0; box-sizing: border-box; }
  html, body {
    width: 1200px; height: 900px; overflow: hidden;
    background: var(--backdrop);
    font-family: "Montserrat", sans-serif;
  }
  .stage { position: relative; width: 1200px; height: 900px; }
  .card {
    position: absolute; left: 300px; width: 600px; height: 343px;
    box-shadow: 0 6px 18px rgba(0,0,0,0.18);
    overflow: hidden;
  }
  /* back side */
  .card-back { top: 64px; background: var(--brand-blue); color: var(--paper); }
  .back-brand {
    position: absolute; top: 108px; left: 0; width: 100%;
    display: flex; justify-content: center; align-items: center; gap: 14px;
  }
  .back-brand .mark { width: 22px; height: 22px; background: var(--paper); }
  .back-brand .name {
    font-weight: 700; font-size: 34px; letter-spacing: 1px; text-transform: uppercase;
  }
  .services {
    position: absolute; top: 250px; left: 0; width: 100%;
    text-align: center; font-size: 12.5px; line-height: 1.55; font-weight: 400;
  }
  .services .divider { color: var(--brand-grey); padding: 0 6px; }
  /* front side */
  .card-front { top: 493px; background: var(--paper); }
  .front-band { position: absolute; inset: 0; }
  .front-brand {
    position: absolute; top: 26px; left: 56px;
    display: flex; align-items: center; gap: 14px;
  }
  .front-brand .mark { width: 30px; height: 30px; background: var(--brand-grey); }
  .front-brand .name {
    font-weight: 700; font-size: 32px; line-height: 1; color: var(--brand-blue);
    text-transform: uppercase; letter-spacing: 0.5px;
  }
  .person {
    position: absolute; top: 92px; right: 36px; text-align: right;
  }
  .person .full-name { font-weight: 700; font-size: 19px; line-height: 1.2; color: var(--brand-blue); }
  .person .role { font-size: 13.5px; color: var(--text-grey); margin-top: 1px; }
  .contacts { list-style: none; margin-top: 10px; }
  .contacts li {
    display: flex; justify-content: flex-end; align-items: center; gap: 6px;
    font-size: 13.5px; color: var(--text-grey); line-height: 1.3;
  }
  .contacts svg { width: 12px; height: 12px; fill: var(--brand-blue); }
  .company {
    position: absolute; bottom: 20px; right: 36px; text-align: right;
    font-size: 13.5px; color: var(--text-grey); line-height: 1.3; font-style: normal;
  }
  .company .company-name { color: var(--brand-blue); font-weight: 500; }
</style>
</head>
<body>
<div class="stage">

  <section class="card card-back">
    <div class="back-brand">
      <span class="mark"></span>
      <span class="name">Vardane Ledger</span>
    </div>
    <p class="services">
      Cryptocurrency Exchange Services<span class="divider">|</span>Cryptocurrency Mining Operations<br>
      Cryptocurrency Investment Fund Offering
    </p>
  </section>

  <section class="card card-front">
    <svg class="front-band" viewBox="0 0 600 343" preserveAspectRatio="none" aria-hidden="true">
      <polygon points="0,0 82,0 74,343 0,343" fill="var(--brand-blue)"/>
    </svg>
    <div class="front-brand">
      <span class="mark"></span>
      <span class="name">Vardane Ledger</span>
    </div>

    <div class="person">
      <p class="full-name">Owen Hadley</p>
      <p class="role">Chief Operations Officer</p>
      <ul class="contacts">
        <li>02 9173 5528
          <svg viewBox="0 0 24 24"><path d="M6.6 10.8a15 15 0 0 0 6.6 6.6l2.2-2.2c.3-.3.7-.4 1-.2 1.1.4 2.3.6 3.6.6.6 0 1 .4 1 1V20c0 .6-.4 1-1 1C10.6 21 3 13.4 3 4c0-.6.4-1 1-1h3.5c.6 0 1 .4 1 1 0 1.3.2 2.5.6 3.6.1.3 0 .7-.2 1z"/></svg>
        </li>
        <li>0418 356 091
          <svg viewBox="0 0 24 24"><path d="M7 1h10a2 2 0 0 1 2 2v18a2 2 0 0 1-2 2H7a2 2 0 0 1-2-2V3a2 2 0 0 1 2-2zm0 3v14h10V4zm5 15.5a1 1 0 1 0 0 2 1 1 0 0 0 0-2z"/></svg>
        </li>
        <li>owen@vardaneledger,com
          <svg viewBox="0 0 24 24"><path d="M2 5h20v14H2zm2 2v.5l8 5 8-5V7zm0 2.9V17h16V9.9l-8 5z"/></svg>
        </li>
        <li>www.vardaneledger,com
          <svg viewBox="0 0 24 24"><path d="M12 2a10 10 0 1 0 0 20 10 10 0 0 0 0-20zm6.9 6h-3a15 15 0 0 0-1.3-3.9A8 8 0 0 1 18.9 8zM12 4c.8 1.2 1.5 2.5 1.9 4h-3.8c.4-1.5 1.1-2.8 1.9-4zM4.3 14a8 8 0 0 1 0-4h3.4a16 16 0 0 0 0 4zm.8 2h3a15 15 0 0 0 1.3 3.9A8 8 0 0 1 5.1 16zm3-8h-3a8 8 0 0 1 4.3-3.9C8.8 5.3 8.4 6.6 8.1 8zM12 20c-.8-1.2-1.5-2.5-1.9-4h3.8c-.4 1.5-1.1 2.8-1.9 4zm2.3-6H9.7a14 14 0 0 1 0-4h4.6a14 14 0 0 1 0 4zm.3 5.9c.6-1.2 1-2.5 1.3-3.9h3a8 8 0 0 1-4.3 3.9zm1.7-5.9a16 16 0 0 0 0-4h3.4a8 8 0 0 1 0 4z"/></svg>
        </li>
      </ul>
    </div>

    <address class="company">
      <span class="company-name">Vardane Ledger Pty Ltd</span><br>
      Level 22, Harbour Point, 48 Wattlebrook Ave<br>
      Sydney NSW 2000<br>
      ABN : 47 318 905 226
    </address>
  </section>

</div>
</body>
</html>
```